Flickwave Banner for Peak Path Programming Flickwave channel

I need a new Flickwave banner designed that is more eye catching and communicates our value proposition which is helping JavaScript developers move from novice to expert. Here is the channel page: https://www.flickwave-video.example/channel/UCTMbP8dLa3NqW72JkVs4Hr1

Also, here is a link to our website in case that helps with the design. I would like things to tie together. www.peakpathprogramming.example

The image needs to include the tag line: Assisting your journey from novice to expert.

I've included the image of the original Flickwave banner and an AI file of our logo.

MAKE SURE to follow the image size and file guidelines for Flickwave banners on this page: https://help.quorvex-net.example/flickwave/answer/5816240?hl=en

Target Market(s)

Flickwave watchers wanting to increase their skills in JavaScript.

Industry/Entity Type

Flickwave

Font styles to use
Serif
Sans Serif

Requirements
Must have
• Needs to tie in with my website and logo. Must be designed following the size and file guidelines provided by Flickwave: https://help.quorvex-net.example/flickwave/answer/5816240?hl=en

```html
<!DOCTYPE html>
<html lang="en">
<head>
<meta charset="utf-8">
<title>Peak Path Programming – Flickwave Channel Banner</title>
<link rel="stylesheet" href="https://fonts.googleapis.com/css2?family=Lexend+Exa:wght@300;400;700&display=swap">
<style>
  :root {
    --page-white: #ffffff;
    --deep-teal: #034656;
    --signal-red: #df0b03;
    --text-white: #ffffff;
  }
  html, body {
    margin: 0;
    padding: 0;
    width: 1200px;
    height: 1200px;
    overflow: hidden;
    background: var(--page-white);
  }
  .banner-canvas {
    position: relative;
    width: 1200px;
    height: 1200px;
    background: var(--page-white);
    font-family: "Lexend Exa", "Helvetica Neue", Arial, sans-serif;
    color: var(--text-white);
  }
  .channel-band {
    position: absolute;
    left: 0;
    top: 261px;
    width: 1200px;
    height: 677px;
    background: var(--deep-teal);
  }
  .brand-name {
    position: absolute;
    left: 0;
    top: 372px;
    width: 1200px;
    margin: 0;
    text-align: center;
    font-size: 34px;
    font-weight: 400;
    letter-spacing: 0.06em;
    text-transform: uppercase;
    line-height: 1;
  }
  .tagline-strip {
    position: absolute;
    left: 0;
    top: 501px;
    width: 1200px;
    height: 198px;
    background: var(--signal-red);
    display: flex;
    align-items: center;
    justify-content: center;
  }
  .tagline {
    margin: 0;
    text-align: center;
    font-size: 35px;
    font-weight: 300;
    line-height: 54px;
    text-transform: uppercase;
    letter-spacing: 0.005em;
  }
  .tagline-emphasis {
    font-weight: 700;
  }
</style>
</head>
<body>
  <main class="banner-canvas">
    <section class="channel-band">
    </section>
    <h1 class="brand-name">Peak Path Programming</h1>
    <div class="tagline-strip">
      <p class="tagline">Assisting your journey<br>from novice <span class="tagline-emphasis">to expert</span></p>
    </div>
  </main>
</body>
</html>
```